Letter and Envelope Design For Larchmont Realty

Please design a letter and an envelope incorporating our logo (See Attached). We are also launched a business card contest. Since we want them to match, please feel free to submit a design for both the business card and also the letter design and envelope.

Requirements
Must have
• The envelope, the letter and the business cards must match somehow connecting the designs. We want them to have something that holds them together besides the logo.

```html
<!DOCTYPE html>
<html lang="en">
<head>
<meta charset="utf-8">
<title>Larchmont Realty – Stationery</title>
<link href="https://fonts.googleapis.com/css2?family=Jost:wght@500&display=swap" rel="stylesheet">
<style>
  :root{
    --stage:#040708;
    --paper:#ffffff;
    --navy:#2b2f86;
    --lilac:#8482b4;
    --stone:#c4c3c4;
    --icon:#5a5a5a;
    --card-back-light:#8d8d8d;
    --card-back-dark:#5e5e5e;
  }
  *{margin:0;padding:0;box-sizing:border-box}
  html,body{width:1200px;height:848px;overflow:hidden;background:var(--stage)}
  body{position:relative;font-family:'Jost',sans-serif;font-weight:500;color:var(--navy)}
  .piece{position:absolute;background:var(--paper);overflow:hidden}
  .piece .shapes{position:absolute;inset:0;width:100%;height:100%}
  .letterhead{left:99px;top:97px;width:455px;height:644px}
  .envelope{left:625px;top:233px;width:454px;height:194px}
  .card-front{left:638px;top:536px;width:206px;height:118px}
  .card-back{left:860px;top:536px;width:204px;height:118px;
    background:radial-gradient(ellipse at 50% 45%,var(--card-back-light),var(--card-back-dark) 75%)}
  .lockup{position:absolute;display:flex;flex-direction:column;align-items:center;text-align:center}
  .lockup .mark{border:2px solid var(--navy);border-radius:50%}
  .lockup .name{color:var(--navy);text-transform:uppercase;line-height:1.15}
  .letterhead .lockup{left:33px;top:20px;width:136px}
  .letterhead .mark{width:52px;height:52px;margin-bottom:6px}
  .letterhead .name{font-size:13px;letter-spacing:2.2px}
  .envelope .lockup{left:17px;top:26px;width:100px}
  .envelope .mark{width:38px;height:38px;margin-bottom:4px}
  .envelope .name{font-size:9.5px;letter-spacing:1.6px}
  .card-front .lockup{left:12px;top:6px;width:76px}
  .card-front .mark{width:27px;height:27px;margin-bottom:3px}
  .card-front .name{font-size:7px;letter-spacing:1px}
  .card-back .lockup{left:42px;top:22px;width:120px}
  .card-back .mark{width:46px;height:46px;margin-bottom:5px}
  .card-back .name{font-size:11px;letter-spacing:1.8px}
  .contact{position:absolute;list-style:none}
  .contact li{display:flex;align-items:center;white-space:nowrap;color:var(--navy)}
  .contact svg{fill:var(--icon);flex:none}
  .letterhead .contact{left:267px;top:30px;font-size:10.4px}
  .letterhead .contact li{height:18.5px}
  .letterhead .contact svg{width:11px;height:11px;margin-right:7px}
  .envelope .contact{left:19px;top:112px;font-size:7.6px}
  .envelope .contact li{height:13.6px}
  .envelope .contact svg{width:9px;height:9px;margin-right:5px}
  .card-front .contact{left:12px;top:64px;font-size:6.2px}
  .card-front .contact li{height:11.6px}
  .card-front .contact svg{width:7px;height:7px;margin-right:5px}
</style>
</head>
<body>
<svg width="0" height="0" style="position:absolute" aria-hidden="true">
  <symbol id="i-pin" viewBox="0 0 24 24"><path d="M12 1a8 8 0 0 0-8 8c0 6 8 14 8 14s8-8 8-14a8 8 0 0 0-8-8zm0 11a3 3 0 1 1 0-6 3 3 0 0 1 0 6z"/></symbol>
  <symbol id="i-phone" viewBox="0 0 24 24"><path d="M6.6 2.5 9.5 6.6 7.6 9a14 14 0 0 0 7.4 7.4l2.4-1.9 4.1 2.9-1.3 3.6c-.3.7-1 1-1.7.9C10 20.6 3.4 14 2.1 5.6c-.1-.7.2-1.4.9-1.7z"/></symbol>
  <symbol id="i-mail" viewBox="0 0 24 24"><path d="M1 4h22v16H1zm2 2v.4l9 7 9-7V6zm18 2.9-6.5 5 6.5 5.1zM3 8.9v10.1l6.5-5.1zm8 6.3L11 15.4 3 18h18l-8-2.6z" fill-rule="evenodd"/></symbol>
  <symbol id="i-web" viewBox="0 0 24 24"><path d="M12 1a11 11 0 1 0 0 22 11 11 0 0 0 0-22zm7.9 10h-3.5a16 16 0 0 0-1.6-7.1A9 9 0 0 1 19.9 11zM12 3.2c1.2 1.6 2.2 4.5 2.4 7.8H9.6c.2-3.3 1.2-6.2 2.4-7.8zM9.2 3.9A16 16 0 0 0 7.6 11H4.1a9 9 0 0 1 5.1-7.1zM4.1 13h3.5a16 16 0 0 0 1.6 7.1A9 9 0 0 1 4.1 13zm7.9 7.8c-1.2-1.6-2.2-4.5-2.4-7.8h4.8c-.2 3.3-1.2 6.2-2.4 7.8zm2.8-.7a16 16 0 0 0 1.6-7.1h3.5a9 9 0 0 1-5.1 7.1z"/></symbol>
</svg>

<section class="piece letterhead" aria-label="Letterhead">
  <svg class="shapes" viewBox="0 0 568 805" preserveAspectRatio="none" aria-hidden="true">
    <polygon fill="var(--stone)" points="81,0 300,0 233,28"/>
    <polygon fill="var(--stone)" points="430,22 568,0 568,12 480,42"/>
    <polygon fill="var(--lilac)" points="221,0 568,0 421,39"/>
    <polygon fill="var(--stone)" points="0,729 97,691 123,722 0,776"/>
    <polygon fill="var(--stone)" points="315,753 388,727 568,805 405,805"/>
    <polygon fill="var(--lilac)" points="0,805 180,683 405,805"/>
  </svg>
  <div class="lockup"><span class="mark"></span><span class="name">Larchmont<br>Realty</span></div>
  <ul class="contact">
    <li><svg><use href="#i-pin"/></svg>Example of a location</li>
    <li><svg><use href="#i-phone"/></svg>2845550174893</li>
    <li><svg><use href="#i-mail"/></svg>Example@yourmail.com</li>
    <li><svg><use href="#i-web"/></svg>www.yourwebsite.com</li>
  </ul>
</section>

<section class="piece envelope" aria-label="Envelope">
  <svg class="shapes" viewBox="0 0 568 243" preserveAspectRatio="none" aria-hidden="true">
    <polygon fill="var(--stone)" points="80,0 300,0 233,28"/>
    <polygon fill="var(--stone)" points="430,24 568,4 568,28 485,42"/>
    <polygon fill="var(--lilac)" points="220,0 568,0 412,45"/>
  </svg>
  <div class="lockup"><span class="mark"></span><span class="name">Larchmont<br>Realty</span></div>
  <ul class="contact">
    <li><svg><use href="#i-pin"/></svg>Example of a location</li>
    <li><svg><use href="#i-phone"/></svg>2845550174893</li>
    <li><svg><use href="#i-mail"/></svg>Example@yourmail.com</li>
    <li><svg><use href="#i-web"/></svg>www.yourwebsite.com</li>
  </ul>
</section>

<section class="piece card-front" aria-label="Business card front">
  <svg class="shapes" viewBox="0 0 257 147" preserveAspectRatio="none" aria-hidden="true">
    <polygon fill="var(--stone)" points="257,0 257,147 225,147 240,40"/>
    <polygon fill="var(--lilac)" points="257,45 257,147 222,100"/>
  </svg>
  <div class="lockup"><span class="mark"></span><span class="name">Larchmont<br>Realty</span></div>
  <ul class="contact">
    <li><svg><use href="#i-pin"/></svg>Example of a location</li>
    <li><svg><use href="#i-phone"/></svg>2845550174893</li>
    <li><svg><use href="#i-mail"/></svg>Example@yourmail.com</li>
    <li><svg><use href="#i-web"/></svg>www.yourwebsite.com</li>
  </ul>
</section>

<section class="piece card-back" aria-label="Business card back">
  <div class="lockup"><span class="mark"></span><span class="name">Larchmont<br>Realty</span></div>
</section>
</body>
</html>
```